■ 依頼の目的/概要

ネットショップで購入者に送付する、「封筒」のデザインを依頼させて頂きます。

ショップURL http://www.pilmo-store.biz

■ 封筒デザインへの要望

女性向けショップなので、清潔感・きれいさを重視します。
ポストを覗いて当ショップのものだとわかるようなデザインが希望です。

■ 封筒の情報

記載
ショップ名(ロゴ) / 会社名 / 住所 / 電話/ URL

サイズ
角2 (240×332)  角6(162×229)

カラー
フルカラーでも、2色でも可

未定 デザイン決定後決めたく思いますが、デザインに対してのオススメがあればご提案ください。

■ 納品ファイルの希望

添付のテンプレートを使用ください。(イラストレーター)
※角2のみのテンプレなので、角6(162×229)はアレンジいただけると幸いです。

■ 進め方

弊社の希望するイメージに近い提案を1つ(場合によって複数)選択させて頂きます。
希望に近づけるために、修正要望を個別にさせて頂くこともあります。
コンペ方式のため、修正後に当選されない場合も、どうかご了承ください。

■ その他/注意点

選択させて頂いたデザインの著作権(財産権)等の扱いはBrivox利用規約に従い、弊社に譲渡をお願いします。フォントや画像素材などを利用する場合は上記利用用途に使用できることを確認し、第三者の知的財産権等に注意して下さい。
ファイルがUPされていなかったのでUPいたします。
多くの方にご提案いただきありがとうございました。

現在選定中ですので結果は今しばらくお待ちいただければと思います。

ご提案いただきました皆様、ありがとうございました。
■ 選んだ理由

女性らしいデザイン、カラー使いから決定させていただきました。

■ 提案者全員のお礼・コメント

数多くのご提案ありがとうございました。

選びかねた作品もございました。

また何かありましたらご依頼したく思います。

```html
<!DOCTYPE html>
<html lang="ja">
<head>
<meta charset="utf-8">
<title>pilmo envelope</title>
<link href="https://fonts.googleapis.com/css2?family=Cormorant+Garamond:wght@500&family=Noto+Sans+JP:wght@400&display=swap" rel="stylesheet">
<style>
  :root {
    --kraft: #c9bb91;
    --kraft-deep: #b5a27c;
    --flap-line: #e2d8b9;
    --brown: #6b4a3a;
  }
  html, body { margin: 0; padding: 0; overflow: hidden; }
  .envelope {
    position: relative;
    width: 814px;
    height: 1200px;
    background: var(--kraft);
    overflow: hidden;
    font-family: "Noto Sans JP", sans-serif;
    color: var(--brown);
  }
  .flap-fold {
    position: absolute;
    left: 0; right: 0; top: 84px;
    height: 2px;
    background: var(--flap-line);
  }
  .ribbon-art {
    position: absolute;
    left: 430px; top: 770px;
    width: 384px; height: 260px;
    background: radial-gradient(ellipse at 70% 50%, var(--kraft-deep) 0%, var(--kraft) 75%);
  }
  .tagline {
    position: absolute;
    left: 120px; top: 862px;
    font-size: 11px;
    line-height: 15px;
    margin: 0;
  }
  .shop-name {
    position: absolute;
    left: 112px; top: 882px;
    margin: 0;
    font-family: "Cormorant Garamond", serif;
    font-weight: 500;
    font-size: 104px;
    line-height: 1;
    letter-spacing: 2px;
    color: var(--brown);
  }
  .shop-url {
    position: absolute;
    left: 200px; top: 990px;
    font-family: "Cormorant Garamond", serif;
    font-size: 17px;
  }
  .address {
    position: absolute;
    left: 120px; top: 1052px;
    font-size: 13px;
    line-height: 20px;
    margin: 0;
    font-style: normal;
  }
  .address .company { margin-bottom: 8px; display: block; }
</style>
</head>
<body>
<div class="envelope">
  <div class="flap-fold"></div>

  <div class="ribbon-art" role="img" aria-label="Brown looping ribbon lettered with the shop name, with a small green heart"></div>

  <p class="tagline">女性のための雑貨セレクトショップ<br>毎日を彩るアイテムをお届けします</p>
  <h1 class="shop-name">pilmo</h1>
  <div class="shop-url">http://www.pilmo-store.biz</div>

  <address class="address">
    <span class="company">pilmo [ピルモ]</span>
    〒150-0001　東京都渋谷区神宮前4-18-7-305<br>
    TEL　03-5412-7730<br>
    Mail　info@pilmo-store.biz
  </address>
</div>
</body>
</html>
```